Real estate company needs a card that makes you say WOW!

We need an awesome business card for our real estate company, Keystone Lakeshore Properties, that will stand out from the crowd. We specialize in buying and selling real estate, property management, and real estate investments (Flips & Rentals). On the business card, I need the following:

- Our logo
- Services
- My name & contact info (Derek Holloway, 630-517-2946, derek@keystonelakeshore.example)
- My title (Director of Acquisitions)
- KeystoneRGC.example

I attached an EPS file of our logo. Let me know if you have any questions. Thank you in advance!

```html
<!DOCTYPE html>
<html lang="en">
<head>
<meta charset="utf-8">
<title>Keystone Lakeshore Properties — Business Card</title>
<link rel="stylesheet" href="https://fonts.googleapis.com/css2?family=Marcellus&display=swap">
<style>
  :root {
    --backdrop: #aebbb8;
    --card-white: #ffffff;
    --brand-blue: #2f6fd6;
    --brand-blue-deep: #1f54c4;
    --brand-blue-light: #4fb3ef;
    --swoosh-grey: #8e9aa0;
    --label-grey: #c9dcf5;
    --shadow: rgba(40, 55, 60, 0.22);
  }
  * { box-sizing: border-box; margin: 0; padding: 0; }
  html, body {
    width: 1200px; height: 800px; overflow: hidden;
    background: var(--backdrop);
    font-family: "Marcellus", "Optima", serif;
  }
  .sheet {
    width: 1200px; height: 800px;
    display: flex; flex-direction: column; align-items: center; justify-content: center;
    gap: 24px;
  }
  .card {
    position: relative;
    width: 640px; height: 366px;
    background: var(--card-white);
    box-shadow: 0 6px 18px var(--shadow);
    overflow: hidden;
  }
  .card-art { position: absolute; inset: 0; width: 100%; height: 100%; }

  .wordmark {
    display: flex; align-items: center; gap: 12px;
    color: var(--brand-blue); white-space: nowrap;
  }
  .wordmark-mark { background: var(--brand-blue); flex: none; }

  /* Back of card */
  .card-back .wordmark {
    position: absolute; left: 0; right: 0; top: 150px;
    justify-content: center; font-size: 36px;
  }
  .card-back .wordmark-mark { width: 22px; height: 22px; }
  .services {
    position: absolute; right: 26px; bottom: 52px;
    font-size: 13px; color: var(--brand-blue); letter-spacing: 0.3px;
  }

  /* Front of card */
  .card-front .wordmark {
    position: absolute; left: 30px; top: 34px; font-size: 22px; gap: 9px;
  }
  .card-front .wordmark-mark { width: 14px; height: 14px; }

  .holder {
    position: absolute; left: 44px; bottom: 42px; color: var(--card-white);
  }
  .holder-name { font-size: 24px; text-transform: uppercase; letter-spacing: 0.5px; }
  .holder-title { font-size: 14px; margin-top: 3px; }

  .contact {
    position: absolute; right: 32px; top: 228px;
    list-style: none; color: var(--card-white); font-size: 14px; line-height: 1.6;
    white-space: nowrap;
  }
  .contact-label { font-size: 10px; color: var(--label-grey); margin-right: 6px; }
</style>
</head>
<body>
<main class="sheet">

  <section class="card card-back" aria-label="Card back">
    <svg class="card-art" viewBox="0 0 640 366" aria-hidden="true">
      <defs>
        <linearGradient id="backBand" x1="0" y1="0" x2="1" y2="0">
          <stop offset="0" stop-color="var(--brand-blue-light)"/>
          <stop offset="1" stop-color="var(--brand-blue-deep)"/>
        </linearGradient>
      </defs>
      <path d="M300 366 Q470 342 640 320 L640 366 Z" fill="url(#backBand)"/>
    </svg>
    <div class="wordmark">
      <span class="wordmark-mark" aria-hidden="true"></span>
      <span class="wordmark-name">Keystone Lakeshore Properties</span>
    </div>
    <p class="services">Buying &amp; Selling · Property Management · Investments</p>
  </section>

  <section class="card card-front" aria-label="Card front">
    <svg class="card-art" viewBox="0 0 640 366">
      <defs>
        <linearGradient id="skylineFill" x1="0" y1="0" x2="0" y2="1">
          <stop offset="0" stop-color="#3f86e6"/>
          <stop offset="1" stop-color="var(--brand-blue-deep)"/>
        </linearGradient>
        <linearGradient id="frontBand" x1="0" y1="1" x2="1" y2="0">
          <stop offset="0" stop-color="var(--brand-blue-light)"/>
          <stop offset="1" stop-color="var(--brand-blue)"/>
        </linearGradient>
      </defs>
      <g role="img" aria-label="City skyline illustration">
        <path d="M0 238 L0 150 L640 70 L640 148 Q300 128 0 238 Z" fill="url(#skylineFill)"/>
      </g>
      <path d="M0 252 Q300 140 640 160 L640 170 Q300 152 0 264 Z" fill="var(--swoosh-grey)"/>
      <path d="M0 276 Q300 162 640 180 L640 366 L0 366 Z" fill="url(#frontBand)"/>
    </svg>
    <div class="wordmark">
      <span class="wordmark-mark" aria-hidden="true"></span>
      <span class="wordmark-name">Keystone Lakeshore Properties</span>
    </div>
    <ul class="contact">
      <li><span class="contact-label">phone</span>630-517-2946</li>
      <li><span class="contact-label">email</span>derek@keystonelakeshore.example</li>
      <li><span class="contact-label">web</span>www.keystonelakeshore.example</li>
    </ul>
    <div class="holder">
      <div class="holder-name">Derek Holloway</div>
      <div class="holder-title">Director of Acquisitions</div>
    </div>
  </section>

</main>
</body>
</html>
```